Thai Takeaway Menu Design

I need a menu re-design for a thai takeaway/restaurant in australia.

Please use content from the existing menu
http://www.forkmapple.example/u/menu/4930267?p=1

I'd like to emphasise on
1 - free delivery for order over $40
2 - gluten free and vegetatian option available on most meal (however you want to word it - not fuss)

*remove (the banner order online and save $10)

I'm happy to change the whole concept & design. I particularly like rustic, raw look more than moden ones. Does not need to be flowery or anything like current one :)

Industry/Entity Type

Restaurant

```html
<!DOCTYPE html>
<html lang="en">
<head>
<meta charset="utf-8">
<title>Maliwan Traditional Thai Cuisine – Menu</title>
<link href="https://fonts.googleapis.com/css2?family=Crimson+Pro:wght@400;500&family=Parisienne&display=swap" rel="stylesheet">
<style>
  :root {
    --red-deep: #7a1613;
    --red-mid: #9b2a22;
    --red-light: #a8342a;
    --cream: #f3e6c8;
    --cream-dark: #dcc49a;
    --ink-brown: #5a2318;
    --price-red: #c0271d;
    --text-light: #f4dcc0;
    --brush: #c9b08c;
    --brush-text: #6b3a26;
  }
  * { margin: 0; padding: 0; box-sizing: border-box; }
  html, body { width: 1200px; height: 927px; overflow: hidden; background: var(--red-deep); }
  .menu {
    position: relative; width: 1200px; height: 927px; overflow: hidden;
    background: radial-gradient(ellipse at 75% 35%, var(--red-light) 0%, var(--red-mid) 40%, var(--red-deep) 100%);
    font-family: "Crimson Pro", Georgia, serif; color: var(--text-light);
  }
  .panel-art { position: absolute; left: 0; top: 0; z-index: 0; }
  .abs { position: absolute; white-space: nowrap; z-index: 1; }

  .section-title {
    position: absolute; z-index: 1; font-family: "Parisienne", cursive; font-size: 28px;
    color: var(--brush-text); line-height: 1;
  }
  .dish-list { position: absolute; z-index: 1; list-style: none; font-size: 16.5px; line-height: 22px; color: var(--ink-brown); }
  .dish-list.centered { text-align: center; }
  .price { position: absolute; z-index: 1; font-size: 17px; color: var(--price-red); }
  .note-red { color: var(--price-red); }

  .brand-name { font-size: 48px; color: var(--text-light); text-align: center; width: 260px; left: 867px; top: 114px; }
  .brand-rule { position: absolute; left: 950px; top: 189px; width: 163px; height: 1px; background: var(--text-light); }
  .brand-tagline { font-size: 20px; left: 807px; width: 380px; text-align: center; top: 203px; }

  .service-line { left: 815px; top: 320px; font-size: 16px; color: #fff; }
  .free-word { left: 815px; top: 342px; font-size: 46px; color: #fff; }
  .free-divider { position: absolute; left: 921px; top: 352px; width: 2px; height: 46px; background: #fff; }
  .free-detail { left: 939px; top: 359px; font-size: 22px; color: #fff; }
  .free-detail b { font-weight: 500; }

  .dietary { right: 18px; top: 424px; text-align: right; font-size: 20px; line-height: 27px; color: var(--text-light); }
  .dietary small { font-size: 17px; }

  .call { left: 58px; top: 812px; font-size: 22px; }
  .call span { font-size: 30px; }
  .hours { left: 415px; top: 775px; font-size: 18px; line-height: 26px; }
  .hours .label { display: block; margin-bottom: 22px; }
  .address { left: 836px; top: 788px; font-size: 18px; line-height: 26px; }
</style>
</head>
<body>
<main class="menu">
  <svg class="panel-art" width="1200" height="927" viewBox="0 0 1200 927">
    <defs>
      <linearGradient id="creamFill" x1="0" y1="0" x2="1" y2="0">
        <stop offset="0" stop-color="#ead6ae"/>
        <stop offset="0.5" stop-color="#f6ebd0"/>
        <stop offset="1" stop-color="#e4cc9f"/>
      </linearGradient>
      <clipPath id="stripClip">
        <path d="M53,86 C300,72 560,70 783,66 L783,304 C560,300 300,306 53,318 Z"/>
      </clipPath>
      <linearGradient id="curryTone" x1="0" y1="0" x2="1" y2="1">
        <stop offset="0" stop-color="#e7e0b8"/><stop offset="1" stop-color="#b9ac6e"/>
      </linearGradient>
      <linearGradient id="noodleTone" x1="0" y1="0" x2="1" y2="1">
        <stop offset="0" stop-color="#f1e5cf"/><stop offset="1" stop-color="#d0855b"/>
      </linearGradient>
      <linearGradient id="rollTone" x1="0" y1="0" x2="1" y2="1">
        <stop offset="0" stop-color="#e6b26c"/><stop offset="1" stop-color="#a4602a"/>
      </linearGradient>
      <radialGradient id="soupTone" cx="0.5" cy="0.5" r="0.5">
        <stop offset="0" stop-color="#f0a458"/><stop offset="0.72" stop-color="#e08a3c"/><stop offset="0.74" stop-color="#ffffff"/><stop offset="1" stop-color="#f1ece6"/>
      </radialGradient>
    </defs>

    <path class="menu-panel" d="M30,48 C260,66 520,62 795,42 L795,752 C560,738 280,742 30,756 Z" fill="url(#creamFill)"/>

    <g clip-path="url(#stripClip)">
      <rect x="53" y="60" width="243" height="270" fill="url(#curryTone)" role="img" aria-label="Photo of green curry chicken"/>
      <rect x="296" y="60" width="226" height="270" fill="url(#noodleTone)" role="img" aria-label="Photo of pad thai with prawns"/>
      <rect x="522" y="60" width="261" height="270" fill="url(#rollTone)" role="img" aria-label="Photo of fried spring rolls"/>
    </g>

    <path d="M73,352 C150,344 260,346 332,350 L326,386 C250,390 150,388 76,384 Z" fill="var(--brush)" opacity="0.85"/>
    <path d="M68,540 C150,532 250,534 326,538 L320,578 C240,582 150,580 72,576 Z" fill="var(--brush)" opacity="0.85"/>
    <path d="M455,400 C530,394 630,396 697,400 L692,438 C620,442 530,440 458,436 Z" fill="var(--brush)" opacity="0.85"/>

    <circle cx="941" cy="628" r="127" fill="url(#soupTone)" role="img" aria-label="Photo of a bowl of red curry soup with an orchid garnish"/>
  </svg>

  <h2 class="section-title" style="left:110px; top:355px;">Dinner for Two</h2>
  <ul class="dish-list" style="left:121px; top:397px;">
    <li>Spring Rolls (4)</li>
    <li>Chicken &amp; Cashew Nuts</li>
    <li>Massaman Curry</li>
    <li>Rice</li>
  </ul>
  <p class="price" style="left:307px; top:481px;">$28</p>

  <h2 class="section-title" style="left:120px; top:542px;">Family Pack</h2>
  <ul class="dish-list" style="left:94px; top:590px;">
    <li>Spring Rolls (4)</li>
    <li>Satay Chicken (4)</li>
    <li>Chicken &amp; Cashew Nuts</li>
    <li style="padding-left:118px;">Red Curry Beef</li>
    <li style="padding-left:118px;">Pad Tahi</li>
    <li style="padding-left:118px;">Rice (L)</li>
  </ul>
  <p class="price" style="left:309px; top:718px;">$45</p>

  <h2 class="section-title" style="left:482px; top:404px;">Lunch Special</h2>
  <ul class="dish-list centered" style="left:438px; width:300px; top:466px;">
    <li>Pad Thai</li>
    <li>Sweet and Sour Pork /w Rice</li>
    <li>Chicken &amp; Cashew Nuts /w Rice</li>
    <li>Green Curry Chicken /w Rice</li>
    <li>Beef Noodle Soup</li>
  </ul>
  <p class="dish-list centered note-red" style="left:438px; width:300px; top:596px;">{Free Can of Soft Drink}</p>
  <p class="price" style="left:684px; top:640px;">$10</p>

  <p class="abs brand-name">Maliwan</p>
  <div class="brand-rule"></div>
  <p class="abs brand-tagline">Maliwan Traditional Thai Cuisine</p>

  <p class="abs service-line">Dine In, Takeaway &amp; Delivery</p>
  <p class="abs free-word">Free</p>
  <div class="free-divider"></div>
  <p class="abs free-detail">delivery for order over <b>$40</b></p>

  <p class="abs dietary">Gluten free <small>and</small> Vegetatian<br><small>option</small> available on most<br>meal</p>

  <p class="abs call">Call: <span>07 3946 1870</span></p>
  <p class="abs hours"><span class="label">Trading Hours</span>Lunch (Wednesday-Sunday) : 11.00 - 2.30PM<br>Dinner (7days) : 5.00 -9.30PM</p>
  <p class="abs address">62 Carrow Street, Riverbend<br>Corner of Elm St. and Carrow Rd.<br>Phone: 07 3946 1870</p>
</main>
</body>
</html>
```